Plakat-Design für Unternehmer- und Marktbund
Zielgruppe
Der Unternehmer- und Marktbund ist ein Verein - Zusammenschluss von Gewerbetreibenden. Im Prinzip wie die Organisation Kreis der Freischaffenden.
Aufgabenstellung
An den Ortseingängen der Gemeinde Wendelsried stehen Ortsinformationstafeln welche immer für den Aufzug von aktuellen Veranstaltungen genutzt werden. Dies sind quasi Stahlträger auf welche Plakate aufgezogen werden. Bisher wurden diese immer wieder abgebaut und aufgebaut. Ziel ist es jetzt, dass die das ganze Jahr über stehen - was nicht so schön aussieht. Deswegen soll hier quasi ein Plakat aufgezogen werden, welches genutzt wird, wenn keine Veranstaltung ansteht.
Auf dem Plakat soll zu sehen sein:
- Logo Gemeinde Wendelsried
- Logo UMB Wendelsried
- Webseite www.umb-wendelsried.de und von der Gemeinde www.wendelsried.de
- Slogan 'Ein starkes Team' gerne sind wir auch für weitere Ideen offen
Informationen von der Firma welche den Druck ausführt
Die Schilder sind 110cm x 160cm, wenn sie das auf einer Plane(Banner) haben wollen, kommen noch 8 Ösen rein, 2cm vom Rand. Die Grafik sollte am besten auf Originalgröße angelegt werden und abspeichern als PDF.

```html
<!DOCTYPE html>
<html lang="de">
<head>
<meta charset="utf-8">
<title>UMB Wendelsried – Ein starkes Team</title>
<link rel="stylesheet" href="https://fonts.googleapis.com/css2?family=Poppins:ital,wght@0,500;0,600;0,700;1,700&display=swap">
<style>
  :root {
    --paper: #f1f1f2;
    --brand-blue: #3b6b9c;
    --headline: #f3f3f3;
    --ink: #3f4146;
    --accent-red: #c8352b;
  }
  html, body {
    margin: 0;
    padding: 0;
    overflow: hidden;
    background: var(--paper);
  }
  .poster {
    position: relative;
    width: 840px;
    height: 1200px;
    background: var(--paper);
    overflow: hidden;
    font-family: "Poppins", sans-serif;
  }
  .header-band {
    position: absolute;
    left: 0; top: 0;
    width: 840px; height: 185px;
    background: var(--paper);
  }
  .club-brand {
    position: absolute;
    left: 46px; top: 58px;
    display: flex;
    align-items: center;
    gap: 16px;
  }
  .club-brand__dot {
    width: 62px; height: 62px;
    border-radius: 50%;
    background: var(--accent-red);
  }
  .club-brand__name {
    font-weight: 600;
    font-size: 30px;
    color: var(--ink);
    letter-spacing: 0.5px;
  }
  .blue-field {
    position: absolute;
    left: 0; top: 185px;
    width: 840px; height: 880px;
    background: var(--brand-blue);
  }
  .municipality-badge {
    position: absolute;
    left: 540px; top: 40px;
    width: 274px; height: 288px;
    background: #ffffff;
    border-radius: 0 0 137px 137px;
    display: flex;
    align-items: center;
    justify-content: center;
    text-align: center;
  }
  .municipality-badge__name {
    font-weight: 600;
    font-size: 24px;
    line-height: 1.25;
    color: var(--ink);
  }
  .slogan {
    position: absolute;
    left: 54px; top: 215px;
    margin: 0;
    font-weight: 700;
    font-style: italic;
    font-size: 158px;
    line-height: 181px;
    color: var(--headline);
    letter-spacing: -2px;
  }
  .town-silhouette {
    position: absolute;
    left: 0; top: 1050px;
    width: 840px; height: 60px;
    background: linear-gradient(to bottom, #e6e8ec, var(--paper));
  }
  .footer-links {
    position: absolute;
    left: 46px; right: 50px; top: 1156px;
    display: flex;
    justify-content: space-between;
    font-weight: 600;
    font-size: 20px;
    color: var(--ink);
  }
</style>
</head>
<body>
  <div class="poster">
    <div class="blue-field"></div>
    <div class="header-band"></div>

    <div class="club-brand">
      <span class="club-brand__dot"></span>
      <span class="club-brand__name">UMB Wendelsried</span>
    </div>

    <div class="municipality-badge">
      <span class="municipality-badge__name">Gemeinde<br>Wendelsried</span>
    </div>

    <h1 class="slogan">Ein<br>starkes<br>Team</h1>

    <div class="town-silhouette" role="img" aria-label="Ortssilhouette mit Kirchturm, Häusern und Baum"></div>

    <div class="footer-links">
      <span>www.umb-wendelsried.de</span>
      <span>www.wendelsried.de</span>
    </div>
  </div>
</body>
</html>
```